Web Design Project - Shipping Industry

Goals and Objectives
The objective of the new website is to create a more modern look and feel. The site will also allow for a more effective means of communicating with members while providing the public with information and developments in the local, regional and international shipping industry.
Scope
The website will highlight the history of the organisation inclusive of text and photographs. It will take visitors through the years from beginning to present. Information on the history of the shipping industry will also be included.
It will feature current articles on the organisation, its members and stakeholders in the shipping industry. Member information as well as pertinent details regarding the organisation’s subsidiaries will be documented for the website.
Information as it relates to shipping statistics, case studies, laws and regulations, international treaties and trade documents, shipping terms, careers in shipping, job opportunities, training opportunities, information for shippers including port listing and trade lanes will be main features of the content for the website.
The Association’s community involvement, industry calendar events and related links relevant industry members will also be featured.
Target Market
• The General Public;
• Members of the organization;
• Shipping Industry Stakeholders (local, regional and international);
• Tertiary students conducting research.
• Potential employees
• Potential Business Partners
Best Practice Bench Marketing
The following websites are being looked at:
• Velloric Docks - http://www.vellori-docks.example/ (preferred look)
• Corvane Maritime Association - http://www.cmx-assoc.example/ (like image transition on main page)
• Trovald - http://www.trovald.example (professional look)
• KBU - http://www.quaylinx.example (preferred color: blue in logo)
• Wuzo - http://www.wuzo.example/electronics/tv-video-audio/ (preferred look for links page: image + short text below + visit site link)
Expected Result
• 3 - 5 pages which must include: [1] main page [2] standard page [3] links page
Target Market(s)
The General Public; Members of the organization; Shipping Industry Stakeholders (local, regional and international); Tertiary students conductin
Industry/Entity Type
Shipping
Look and feel

```html
<!DOCTYPE html>
<html lang="en">
<head>
<meta charset="utf-8">
<title>Shipping Industry</title>
<link href="https://fonts.googleapis.com/css2?family=Open+Sans:wght@400;600;700&family=Roboto+Condensed:wght@700&family=Ubuntu:wght@500;700&display=swap" rel="stylesheet">
<style>
:root{
  --page-bg:#ececec;
  --sheet:#f7f7f7;
  --blue:#0b47b8;
  --blue-dark:#0a3a96;
  --nav-blue:#1050c8;
  --ink:#333;
  --muted:#555;
  --grey-head:#555;
  --panel:#23262b;
  --rule:#cfcfcf;
  --footer-top:#5a5a5a;
  --footer-bot:#2e2e2e;
}
*{box-sizing:border-box;margin:0;padding:0}
html,body{width:1114px;height:1200px;overflow:hidden}
body{background:var(--page-bg);font-family:"Open Sans",sans-serif;color:var(--ink);position:relative}
.sheet{position:absolute;left:95px;top:0;width:924px;height:1200px;background:linear-gradient(#f9f9f9,#f3f3f3)}
.abs{position:absolute}

/* navigation */
.main-nav{position:absolute;left:110px;top:0;width:895px;height:36px;display:flex;background:linear-gradient(#1f66e0,#0a42b0);clip-path:polygon(0 0,100% 0,98.4% 100%,1.6% 100%)}
.main-nav a{color:#fff;text-decoration:none;font-family:"Ubuntu",sans-serif;font-weight:500;font-size:12.5px;display:flex;align-items:center;justify-content:center;border-right:1px solid #0a3a96;letter-spacing:.3px}
.main-nav a.current{background:linear-gradient(#4a4a4a,#1c1c1c)}

/* brand */
.brand{left:112px;top:62px;display:flex;align-items:center;gap:14px}
.brand-mark{width:72px;height:72px;background:var(--blue)}
.brand-name{font-family:"Ubuntu",sans-serif;font-weight:700;font-size:44px;color:var(--blue);letter-spacing:.5px}

/* hero */
.hero-frame{left:112px;top:160px;width:894px;height:352px;background:#fff;border:1px solid #ddd}
.hero-photo{left:119px;top:166px;width:882px;height:341px;background:linear-gradient(#9fc6e0 0%,#6a8da5 8%,#1f5d92 12%,#1a4f80 60%,#143f68 100%)}
.hero-panel{left:670px;top:116px;width:312px;height:380px}
.search{left:722px;top:130px;width:228px;height:29px;background:#fff;border-radius:4px;display:flex;align-items:center;overflow:hidden}
.search span{flex:1;font-size:11px;color:#999;padding-left:16px}
.search b{width:36px;height:29px;background:linear-gradient(#eee,#bbb);display:flex;align-items:center;justify-content:center}
.panel-title{left:716px;top:176px;font-family:"Ubuntu",sans-serif;font-weight:700;font-size:35px;color:#1a66ff}
.panel-sub{left:719px;top:224px;width:250px;font-family:"Ubuntu",sans-serif;font-weight:700;font-size:17px;line-height:21px;color:#fff}
.panel-copy{left:719px;top:272px;width:238px;font-size:11.5px;line-height:18.6px;color:#fff;text-align:justify}
.more-btn{left:768px;top:420px;width:146px;height:35px;background:linear-gradient(#2a7cff,#0a43b8);clip-path:polygon(8% 0,92% 0,100% 50%,92% 100%,8% 100%,0 50%);color:#fff;font-family:"Ubuntu",sans-serif;font-weight:700;font-size:14.5px;display:flex;align-items:center;justify-content:center}

/* columns */
.col{top:529px;height:302px}
.col-divider{position:absolute;top:532px;height:300px;border-left:1px dotted #bbb}
.col-head{display:flex;align-items:center;gap:8px;font-family:"Roboto Condensed",sans-serif;font-weight:700;font-size:21px;color:var(--grey-head)}
.col-head em{font-style:normal;color:var(--blue)}
.col p{font-size:11.5px;line-height:17px;color:var(--muted);text-align:justify;letter-spacing:.2px}
.col p strong{color:#333;font-weight:600}
.bullets{list-style:none;font-size:11.5px;color:#444;letter-spacing:.3px}
.bullets li{position:relative;padding-left:20px}
.bullets li::before{content:"";position:absolute;left:3px;top:6px;width:6px;height:6px;background:var(--blue-dark)}
.more{position:absolute;right:0;font-size:11.5px;font-weight:700;color:var(--blue-dark);text-decoration:none}
.section-rule{left:95px;top:832px;width:924px;border-top:1px dotted #bbb}

/* association */
.assoc-head{left:105px;top:849px;display:flex;align-items:center;gap:8px;font-family:"Roboto Condensed",sans-serif;font-weight:700;font-size:21px;color:var(--grey-head)}
.assoc-head em{font-style:normal;color:var(--blue)}
.arrows{left:952px;top:862px;display:flex;gap:6px}
.arrows span{width:24px;height:24px;display:flex;align-items:center;justify-content:center}
.card{top:910px;width:160px}
.card-frame{height:125px;background:#fff;border:1px solid #ddd;border-radius:8px;padding:5px}
.card-photo{height:114px;border-radius:4px}
.card p{margin-top:6px;font-size:10.5px;line-height:15px;color:#444}
.card .price{margin-top:3px}
.card .price b{color:var(--blue-dark)}

/* footer */
.site-footer{left:96px;top:1126px;width:922px;height:74px;background:linear-gradient(var(--footer-top),var(--footer-bot));color:#fff;text-align:center;font-family:"Ubuntu",sans-serif;font-size:11px;letter-spacing:.4px}
.footer-nav{margin-top:11px;font-weight:500}
.footer-nav a{color:#fff;text-decoration:none;padding:0 8px}
.site-footer p{margin-top:6px}
</style>
</head>
<body>
<div class="sheet"></div>

<nav class="main-nav">
  <a class="current" href="#" style="width:104px">HOME</a>
  <a href="#" style="width:91px">NEWS</a>
  <a href="#" style="width:107px">CAREER</a>
  <a href="#" style="width:165px">SUBSTAINABILTY</a>
  <a href="#" style="width:100px">ISSUES</a>
  <a href="#" style="width:96px">LINKS</a>
  <a href="#" style="width:135px;border-right:0">CONTACT US</a>
</nav>

<header class="abs brand">
  <div class="brand-mark"></div>
  <div class="brand-name">Shipping Industry</div>
</header>

<div class="abs hero-frame"></div>
<div class="abs hero-photo" role="img" aria-label="Photo of a white cruise ship sailing on deep blue sea with hills behind"></div>

<svg class="abs hero-panel" viewBox="0 0 312 380" aria-hidden="true">
  <defs><linearGradient id="pg" x1="0" y1="0" x2="0" y2="1"><stop offset="0" stop-color="#2d3036"/><stop offset="1" stop-color="#1b1d21"/></linearGradient></defs>
  <path d="M2 48 Q2 10 20 2 L290 2 Q310 10 310 48 L310 350 L156 378 L2 350 Z" fill="url(#pg)" stroke="#e8e8e8" stroke-width="3"/>
  <path d="M150 358 L162 358 L156 365 Z" fill="#ddd"/>
</svg>
<div class="abs search"><span>Enter Keyword</span><b><svg width="18" height="18" viewBox="0 0 18 18"><circle cx="11" cy="7" r="5" fill="none" stroke="#777" stroke-width="1.5"/><path d="M7.5 10.5 L2 16" stroke="#777" stroke-width="2"/></svg></b></div>
<div class="abs panel-title">Shipping</div>
<div class="abs panel-sub">Challenges that dare you to push yourself.</div>
<p class="abs panel-copy">Lorem Ipsum is simply dummy text of the printing and typesetting industry. Lorem Ipsum has been the industry's standard dummy text ever since the 1500s, when an unknown printer took a galley of type and scrambled it to make a type specimen book.make a type specimen book.</p>
<a class="abs more-btn">More Details</a>

<!-- How we work -->
<section class="abs col" style="left:112px;width:263px">
  <h2 class="col-head">
    <svg width="44" height="46" viewBox="0 0 44 46"><rect x="16" y="0" width="8" height="8" fill="#111"/><rect x="10" y="8" width="22" height="10" fill="#111"/><path d="M2 20 H42 L36 36 H8 Z" fill="#111"/><path d="M2 40 q5 -4 10 0 t10 0 t10 0 t10 0" fill="none" stroke="#111" stroke-width="2.5"/></svg>
    <span><em>How we</em> Work</span>
  </h2>
  <div role="img" aria-label="Photo of a blue container ship at sea" style="margin:2px 0 0 4px;width:251px;height:128px;background:linear-gradient(#dfe9f3 0%,#b9cde0 55%,#3e6f9e 70%,#2b5785 100%)"></div>
  <p style="margin-top:12px"><strong>Lorem Ipsum is simply dummy text of the printing and typesetting</strong> industry. Lorem Ipsum has been the industry's standard dummy text ever since standard dummy text ever since</p>
  <a class="more" style="top:272px;right:-10px">Moreinfo[+]</a>
</section>
<div class="col-divider" style="left:395px"></div>

<!-- Our services -->
<section class="abs col" style="left:418px;width:264px">
  <h2 class="col-head">
    <svg width="62" height="40" viewBox="0 0 62 40"><rect x="12" y="12" width="4" height="10" fill="#111"/><rect x="20" y="10" width="4" height="12" fill="#111"/><rect x="28" y="12" width="4" height="10" fill="#111"/><rect x="36" y="14" width="4" height="8" fill="#111"/><path d="M0 22 H62 L56 34 H4 Z" fill="#111"/></svg>
    <span><em>Our</em> Services</span>
  </h2>
  <p style="margin-top:10px"><strong>Lorem Ipsum is simply dummy text of the printing and typesetting</strong> industry. Lorem Ipsum has been the industry's standard dummy text ever since</p>
  <p style="margin-top:10px">Lorem Ipsum has been the industry's standard dummy text ever since</p>
  <ul class="bullets" style="margin-top:8px;line-height:20.5px">
    <li>Sharpening their focus on strategic goals</li>
    <li>Better management of operating costs</li>
    <li>Filling gaps in technical expertise</li>
    <li>Boosting system performance</li>
  </ul>
  <a class="more" style="top:272px;right:-12px">Moreinfo[+]</a>
</section>
<div class="col-divider" style="left:722px"></div>

<!-- Why us -->
<section class="abs col" style="left:733px;width:270px">
  <h2 class="col-head">
    <svg width="50" height="50" viewBox="0 0 50 50"><g stroke="#111" stroke-width="3"><circle cx="25" cy="25" r="14" fill="none"/><path d="M25 2 V48 M2 25 H48 M9 9 L41 41 M41 9 L9 41"/></g><circle cx="25" cy="25" r="5" fill="#111"/></svg>
    <span><em>Why</em> us !</span>
  </h2>
  <ul class="bullets" style="margin-top:4px;line-height:27.3px">
    <li>Sharpening their focus on strategic goals</li>
    <li>Better management of operating costs</li>
    <li>Filling gaps in technical expertise</li>
    <li>Boosting system performance</li>
    <li>Sharpening their focus on strategic goals</li>
    <li>Better management of operating costs</li>
    <li>Filling gaps in technical expertise</li>
    <li>Boosting system performance</li>
  </ul>
  <a class="more" style="top:272px;right:0">Moreinfo[+]</a>
</section>

<div class="abs section-rule"></div>

<h2 class="abs assoc-head">
  <svg width="40" height="40" viewBox="0 0 40 40"><defs><linearGradient id="bg" x1="0" y1="0" x2="0" y2="1"><stop offset="0" stop-color="#5aa8f0"/><stop offset="1" stop-color="#0a4fb0"/></linearGradient></defs><circle cx="20" cy="20" r="18" fill="url(#bg)"/><path d="M8 22 H32 L28 28 H12 Z M14 17 H26 V22 H14 Z" fill="#fff"/></svg>
  <span><em>About The Shipping</em> Association</span>
</h2>
<div class="abs arrows">
  <span style="background:var(--blue-dark)"><svg width="12" height="14" viewBox="0 0 12 14"><path d="M9 1 L3 7 L9 13" fill="none" stroke="#fff" stroke-width="3"/></svg></span>
  <span style="background:#666"><svg width="12" height="14" viewBox="0 0 12 14"><path d="M3 1 L9 7 L3 13" fill="none" stroke="#fff" stroke-width="3"/></svg></span>
</div>

<article class="abs card" style="left:111px"><div class="card-frame"><div class="card-photo" role="img" aria-label="Photo of a red ship bow with an aircraft above and containers" style="background:linear-gradient(#bfe0f4 0%,#9fcbe9 50%,#c9443a 70%,#a83028 100%)"></div></div><p>Local marine and cargo surveyor and claims settling agents,</p><p class="price">New from &nbsp;: &nbsp;<b>$29.99</b></p></article>
<article class="abs card" style="left:293px"><div class="card-frame"><div class="card-photo" role="img" aria-label="Photo of a container ship beside blue port cranes" style="background:linear-gradient(#cfe4f2 0%,#a9cde6 55%,#3a7fb5 75%,#2c6a9c 100%)"></div></div><p>Local marine and cargo surveyor and claims settling agents,</p><p class="price">New from &nbsp;: &nbsp;<b>$29.99</b></p></article>
<article class="abs card" style="left:473px"><div class="card-frame"><div class="card-photo" role="img" aria-label="Aerial photo of a loaded container ship at sea" style="background:linear-gradient(#6b8597 0%,#506e84 40%,#8b5a55 60%,#3c5a70 100%)"></div></div><p>Local marine and cargo surveyor and claims settling agents,</p><p class="price">New from &nbsp;: &nbsp;<b>$29.99</b></p></article>
<article class="abs card" style="left:658px"><div class="card-frame"><div class="card-photo" role="img" aria-label="Photo of a container terminal at dusk" style="background:linear-gradient(#d8d2c8 0%,#b39070 40%,#7a4a30 65%,#3b3a3a 100%)"></div></div><p>Local marine and cargo surveyor and claims settling agents,</p><p class="price">New from &nbsp;: &nbsp;<b>$29.99</b></p></article>
<article class="abs card" style="left:843px"><div class="card-frame"><div class="card-photo" role="img" aria-label="Photo of a lit container port at night" style="background:linear-gradient(#2a67c8 0%,#1d4fa6 45%,#c98a3a 62%,#173a7a 100%)"></div></div><p>Local marine and cargo surveyor and claims settling agents,</p><p class="price">New from &nbsp;: &nbsp;<b>$29.99</b></p></article>

<footer class="abs site-footer">
  <nav class="footer-nav"><a>HOME</a>|<a>NEWS</a>|<a>CAREER</a>|<a>SUBSTAINABILTY</a>|<a>ISSUES</a>|<a>LINKS</a>|<a>CONTACT US</a></nav>
  <p>© copyright 2004 Harbourline Shipping Association</p>
  <p>Powered by:Brightwave Studio Ltd</p>
</footer>
</body>
</html>
```